Product Setup Instructional Infographic/flyer

Converting product instructions into an infographic. Would prefer that the instructions fit on a 4x6 card, front and back, but a slightly larger size is acceptable as well.

Logo Text

Ridgeline Cask (Rebranding just as Ridgeline Cask, instead of Ridgeline Cask Barrels)

Font styles to use
Decorative

Colors

Designer to choose colors to be used in the design.

Requirements
Must have
• NA
Nice to have
• NA
Should not have
• NA

```html
<!DOCTYPE html>
<html lang="en">
<head>
<meta charset="utf-8">
<title>Ridgeline Cask – Barrel Curing Steps</title>
<link rel="stylesheet" href="https://fonts.googleapis.com/css2?family=Macondo&family=Alfa+Slab+One&display=swap">
<style>
  :root {
    --bg-dark: #140d0a;
    --bg-mid: #2a1c14;
    --bg-foliage: #2f3a1c;
    --wood-light: #b0481c;
    --wood-mid: #8a3413;
    --wood-dark: #5c200b;
    --bubble-edge: #e9d7c4;
    --badge-light: #8a5a34;
    --badge-dark: #3d2412;
    --step-gold: #f0b632;
    --step-shadow: #3a1c08;
    --text-cream: #fbf1e4;
  }
  * { margin: 0; padding: 0; box-sizing: border-box; }
  html, body { width: 857px; height: 1200px; overflow: hidden; background: var(--bg-dark); }
  .card {
    position: relative;
    width: 857px;
    height: 1200px;
    overflow: hidden;
    font-family: "Macondo", fantasy;
  }
  .backdrop {
    position: absolute; inset: 0;
    background:
      radial-gradient(ellipse 60% 40% at 85% 85%, rgba(70,90,40,.55), transparent 70%),
      radial-gradient(ellipse 50% 35% at 10% 75%, rgba(60,70,35,.45), transparent 70%),
      radial-gradient(ellipse 70% 40% at 50% 20%, rgba(70,45,30,.55), transparent 75%),
      linear-gradient(180deg, var(--bg-mid) 0%, var(--bg-dark) 45%, #1a170f 75%, var(--bg-foliage) 100%);
  }
  .shapes { position: absolute; inset: 0; }
  .step-text {
    position: absolute;
    color: var(--text-cream);
    font-size: 21px;
    line-height: 36px;
    white-space: nowrap;
  }
  .step-1 { left: 129px; top: 94px; }
  .step-2 { left: 236px; top: 348px; }
  .step-3 { left: 143px; top: 622px; }
  .step-tips { left: 229px; top: 836px; line-height: 35.5px; }
  .badge-word {
    font-family: "Alfa Slab One", serif;
    fill: var(--step-gold);
    stroke: var(--step-shadow);
    stroke-width: 1.5;
    paint-order: stroke;
  }
  .badge-num {
    font-family: "Macondo", fantasy;
    font-style: italic;
    fill: var(--text-cream);
  }
</style>
</head>
<body>
<main class="card">
  <div class="backdrop" role="img" aria-label="Dark photo of stacked oak barrels fading into moss-draped trees"></div>

  <svg class="shapes" width="857" height="1200" viewBox="0 0 857 1200">
    <defs>
      <linearGradient id="wood" x1="0" y1="0" x2="1" y2="1">
        <stop offset="0" stop-color="var(--wood-light)"/>
        <stop offset=".5" stop-color="var(--wood-mid)"/>
        <stop offset="1" stop-color="var(--wood-dark)"/>
      </linearGradient>
      <radialGradient id="badge" cx=".45" cy=".4" r=".65">
        <stop offset="0" stop-color="var(--badge-light)"/>
        <stop offset="1" stop-color="var(--badge-dark)"/>
      </radialGradient>
      <path id="tips-arc" d="M52,945 A46,46 0 0 1 144,945"/>
    </defs>

    <g class="bubbles" fill="url(#wood)" stroke="var(--bubble-edge)" stroke-width="1.5">
      <path d="M130,78 H648 Q678,78 678,108 V259 Q678,289 648,289 H140 L25,272 L100,240 V108 Q100,78 130,78 Z"/>
      <path d="M241,329 H730 Q760,329 760,359 V490 L836,530 L745,549 H241 Q211,549 211,519 V359 Q211,329 241,329 Z"/>
      <path d="M157,599 H664 Q694,599 694,629 V734 Q694,764 664,764 H150 L51,750 L127,720 V629 Q127,599 157,599 Z"/>
      <path d="M211,823 H730 Q760,823 760,853 V1010 L840,1051 L740,1072 H211 Q181,1072 181,1042 V853 Q181,823 211,823 Z"/>
    </g>

    <g class="badges" fill="url(#badge)">
      <circle cx="749" cy="196" r="53"/>
      <circle cx="137" cy="439" r="53"/>
      <circle cx="770" cy="688" r="53"/>
      <circle cx="97" cy="941" r="55"/>
    </g>

    <g class="badge-labels" text-anchor="middle">
      <text class="badge-word" x="749" y="196" font-size="30">Step</text>
      <text class="badge-num" x="745" y="230" font-size="32">05</text>
      <text class="badge-word" x="138" y="439" font-size="30">Step</text>
      <text class="badge-num" x="134" y="473" font-size="32">06</text>
      <text class="badge-word" x="770" y="688" font-size="30">Step</text>
      <text class="badge-num" x="766" y="722" font-size="32">07</text>
      <text class="badge-word" font-size="17"><textPath href="#tips-arc" startOffset="50%">Additional</textPath></text>
      <text class="badge-word" x="97" y="950" font-size="26">Tips</text>
    </g>
  </svg>

  <p class="step-text step-1">Using a funnel, fill the barrel with hot water<br>until it is full. Leave the top hole open. Your barrel<br>might leak, and that’s OK. It is not watertight<br>yet and this process will make the wood expand to<br>seal the gaps.</p>

  <p class="step-text step-2">Leave the barrel this way until no more leakages<br>&nbsp;can be seen. This means the wood has expanded<br>andthe gaps are sealed. This can take from<br>30 minutes to an entire week, depending on the<br>size of the barrel.</p>

  <p class="step-text step-3">Drain the barrel and let it air dry for no more than<br>four hours. After 4 hours, it is ready to be filled with<br>any spirits or wine of your choice.</p>

  <p class="step-text step-tips">If you plan on aging different kinds of alcohol<br>using the same barrel, you must cure the barrel<br>again<br>(Step 6) for three to five days. This will allow<br>the barrel to absorb enough water and prevent<br>the next</p>
</main>
</body>
</html>
```